Retractable Banners Designs for Tradeshows

We like the look and feel of the banners draft but want a more polished and improved version of the banners

The dimensions of each banner should be 33" x 80"

We want the banners to work on their own as they will be used in different places, but at tradeshows, they might be used side by side in a 10x10 tradeshow booth, so common design elements that work together is needed.
Updates

Low design quality

Target Market(s)

tradeshows booths

Colors
EB3D1F
EC4F4E
F09395
F8D3D4
FCEDEE

Requirements
Must have
• Elements that tie all the banners together, large scale images, not to cluttered or busy, designed to be visible and attractive from far away, our corporate colours are red, black, white and gray
Nice to have
• bright design not dark but using our corporate colours of red, gray, white and some black

```html
<!DOCTYPE html>
<html lang="en">
<head>
<meta charset="utf-8">
<title>Northwave Tradeshow Banner Set</title>
<link rel="stylesheet" href="https://fonts.googleapis.com/css2?family=Open+Sans:wght@400;600;800&display=swap">
<style>
  :root {
    --stage: #434f52;
    --red-light: #d8232f;
    --red-deep: #8c0e1b;
    --red-line: #e01f26;
    --charcoal: rgba(30, 30, 30, 0.9);
    --white: #ffffff;
    --sky: #3d83e0;
    --server: #6c8592;
    --lab: #3a3a3c;
    --field: #8a8f96;
  }
  * { box-sizing: border-box; margin: 0; padding: 0; }
  html, body { width: 1200px; height: 849px; overflow: hidden; }
  body {
    background: var(--stage);
    font-family: "Open Sans", Arial, sans-serif;
    color: var(--white);
    position: relative;
  }
  .banner {
    position: absolute;
    top: 121px;
    width: 240px;
    height: 582px;
    overflow: hidden;
  }
  .banner--telecom { left: 80px; }
  .banner--ict { left: 344px; }
  .banner--test { left: 608px; }
  .banner--hardware { left: 873px; }

  .banner__photo { position: absolute; inset: 0; }
  .banner--telecom .banner__photo { background: linear-gradient(180deg, #2f78dc, #5a9cf0 60%, #3a6fc2); }
  .banner--ict .banner__photo { background: linear-gradient(180deg, #b9d3d6, #4f6978 30%, #2c3940 75%, #9fc4c5); }
  .banner--test .banner__photo { background: linear-gradient(180deg, #202022, #55585c 40%, #2a2a2c 80%, #101010); }
  .banner--hardware .banner__photo { background: linear-gradient(160deg, #a0a8b0, #6e7378 50%, #9aa3ad); }

  .banner__shapes { position: absolute; inset: 0; width: 240px; height: 582px; }

  .brand {
    position: absolute;
    left: 20px;
    top: 54px;
    font-size: 19px;
    font-weight: 400;
    letter-spacing: 0.2px;
    color: var(--white);
  }
  .banner__title {
    position: absolute;
    left: 20px;
    top: 318px;
    font-size: 21px;
    font-weight: 800;
    line-height: 26px;
    text-transform: uppercase;
  }
  .banner__rule {
    position: absolute;
    left: 20px;
    width: 200px;
    height: 1px;
    background: var(--white);
  }
  .banner__tagline {
    position: absolute;
    left: 20px;
    width: 210px;
    font-size: 20px;
    font-weight: 400;
    line-height: 23.5px;
  }
  .banner__url {
    position: absolute;
    right: 16px;
    top: 514px;
    font-size: 8.5px;
    font-weight: 600;
    letter-spacing: 0.3px;
  }
</style>
</head>
<body>

<svg width="0" height="0" style="position:absolute">
  <defs>
    <linearGradient id="redBand" x1="0" y1="0" x2="1" y2="0">
      <stop offset="0" stop-color="#d8232f"/>
      <stop offset="1" stop-color="#8c0e1b"/>
    </linearGradient>
  </defs>
</svg>

<!-- Banner 1 -->
<section class="banner banner--telecom">
  <div class="banner__photo" role="img" aria-label="Photo of a telecom tower with panel antennas against a blue sky"></div>
  <svg class="banner__shapes" viewBox="0 0 240 582">
    <polygon points="0,32 240,18 240,77 0,135" fill="url(#redBand)"/>
    <polygon points="0,293 240,329 240,527 0,566" fill="url(#redBand)" opacity="0.93"/>
    <line x1="0" y1="282" x2="240" y2="325" stroke="var(--red-line)" stroke-width="2"/>
    <line x1="0" y1="520" x2="240" y2="482" stroke="#ffffff" stroke-opacity="0.6" stroke-width="1.5"/>
  </svg>
  <div class="brand">northwave</div>
  <h2 class="banner__title">Telecom<br>Infrastructure</h2>
  <div class="banner__rule" style="top:380px"></div>
  <p class="banner__tagline" style="top:390px">Cutting Edge Solution for the Next Generation.</p>
  <div class="banner__url">www.northwavesystems.com</div>
</section>

<!-- Banner 2 -->
<section class="banner banner--ict">
  <div class="banner__photo" role="img" aria-label="Photo of server racks in a data centre"></div>
  <svg class="banner__shapes" viewBox="0 0 240 582">
    <polygon points="0,32 240,18 240,77 0,135" fill="var(--charcoal)"/>
    <polygon points="0,293 240,329 240,527 0,566" fill="var(--charcoal)"/>
    <line x1="0" y1="282" x2="240" y2="325" stroke="#ffffff" stroke-opacity="0.7" stroke-width="2"/>
    <line x1="0" y1="520" x2="240" y2="482" stroke="#ffffff" stroke-opacity="0.6" stroke-width="1.5"/>
  </svg>
  <div class="brand">northwave</div>
  <h2 class="banner__title">ICT<br>Solutions</h2>
  <div class="banner__rule" style="top:380px"></div>
  <p class="banner__tagline" style="top:390px">Seamless Cable and Telecom Networks and Enterprise Deployments.</p>
  <div class="banner__url">www.northwavesystems.com</div>
</section>

<!-- Banner 3 -->
<section class="banner banner--test">
  <div class="banner__photo" role="img" aria-label="Photo of test and measurement instruments on a lab bench"></div>
  <svg class="banner__shapes" viewBox="0 0 240 582">
    <polygon points="0,32 240,18 240,77 0,135" fill="url(#redBand)"/>
    <polygon points="0,293 240,329 240,527 0,566" fill="url(#redBand)" opacity="0.93"/>
    <line x1="0" y1="282" x2="240" y2="325" stroke="var(--red-line)" stroke-width="2"/>
    <line x1="0" y1="520" x2="240" y2="482" stroke="#ffffff" stroke-opacity="0.6" stroke-width="1.5"/>
  </svg>
  <div class="brand">northwave</div>
  <h2 class="banner__title">Test &amp;<br>Measurement</h2>
  <div class="banner__rule" style="top:380px"></div>
  <p class="banner__tagline" style="top:390px">Accurate and Efficient Solutions for the Wireless World.</p>
  <div class="banner__url">www.northwavesystems.com</div>
</section>

<!-- Banner 4 -->
<section class="banner banner--hardware">
  <div class="banner__photo" role="img" aria-label="Photo of a technician installing radio equipment on a mast"></div>
  <svg class="banner__shapes" viewBox="0 0 240 582">
    <polygon points="0,32 240,18 240,77 0,135" fill="var(--charcoal)"/>
    <polygon points="0,293 240,329 240,527 0,566" fill="var(--charcoal)"/>
    <line x1="0" y1="282" x2="240" y2="325" stroke="#ffffff" stroke-opacity="0.7" stroke-width="2"/>
    <line x1="0" y1="520" x2="240" y2="482" stroke="#ffffff" stroke-opacity="0.6" stroke-width="1.5"/>
  </svg>
  <div class="brand">northwave</div>
  <h2 class="banner__title">Hareware</h2>
  <div class="banner__rule" style="top:351px"></div>
  <p class="banner__tagline" style="top:364px">High-Quality, Economical. Test Grade RF and Microwave Components.</p>
  <div class="banner__url">www.northwavesystems.com</div>
</section>

</body>
</html>
```